Website Design for Firefighter Apparel Company

Design a bold firefighter themed website that I will be selling apparel on. T shirts, hats, hoodies.

Name of the Company: Brisk Pails Apparel

I need a fully functional, coded and worked Wix website for my apparel company launch in the near future.

I want the theme to be bold and firefighter related, the use of smoky backgrounds, fire, ladders, hose, fire hydrants, reds, blacks, grey and white colors. I’ve uploaded a design that will be one of our t shirt designs, I like the rustic, traditional style artwork.

It needs a “Home” Page, “Shop” Page, and “Our Story” Page. The “Shop” page needs to have a drop down menu with subcategories of: “Men’s Tees”, “Hats” “Hoodies” and “Accessories”

The bottom of the site needs to hold an area where media links like , Instagram, Tik Tok can be placed.

Target Market(s)

Firefighters, working class

Industry/Entity Type

Apparel Company - Firefighter Themed

Coding

Coded - Design and coding required

Requirements
Must have
• Logo, easy accessibility/navigation. Fire themed A fully working e-commerce site, ready to accept payments. This is all through wix.

```html
<!DOCTYPE html>
<html lang="en">
<head>
<meta charset="utf-8">
<title>Brisk Pails Apparel</title>
<link rel="stylesheet" href="https://fonts.googleapis.com/css2?family=Poppins:wght@300;400;500;600;700;800&display=swap">
<style>
:root{
  --red:#cc1430;
  --red-dark:#a80f25;
  --pink:#e07b8c;
  --ink:#111111;
  --text:#555555;
  --grey-bg:#e2e2e2;
  --card-grey:#cfcfcf;
  --white:#ffffff;
  --dark:#0b0b0b;
}
*{box-sizing:border-box;margin:0;padding:0}
html,body{width:1200px;height:4060px;overflow:hidden}
body{font-family:"Poppins",sans-serif;color:var(--ink);background:var(--white);position:relative}
.abs{position:absolute}
.btn{position:absolute;background:var(--red);color:var(--white);font-size:13px;font-weight:600;display:flex;align-items:center;justify-content:center;gap:8px;border-radius:3px;box-shadow:0 4px 10px rgba(204,20,48,.35)}
.ph{position:absolute}

/* header */
.site-header{position:absolute;left:0;top:0;width:1200px;height:84px;background:rgba(40,44,50,.85);z-index:3}
.brand{position:absolute;left:162px;top:26px;color:var(--white);font-weight:700;font-size:17px;letter-spacing:.5px;line-height:1.1}
.nav{position:absolute;top:34px;left:384px;display:flex;gap:0;font-size:13px;color:#b9bcc2}
.nav a{position:absolute;white-space:nowrap;color:inherit;text-decoration:none}
.nav a.active{color:var(--white);font-weight:600}
.search{position:absolute;left:803px;top:22px;width:50px;height:38px;border:1px solid #8a8f96;border-radius:3px;display:flex;align-items:center;justify-content:center}

/* hero */
.hero{position:absolute;left:0;top:0;width:1200px;height:675px;background:radial-gradient(ellipse at 60% 45%,#5a5f66 0%,#353a41 40%,#1c1f24 100%)}
.hero h1{position:absolute;left:162px;top:195px;color:var(--white);font-weight:300;font-size:66px;line-height:80px;letter-spacing:.5px}
.hero h1 b{font-weight:700;position:relative;display:inline-block}
.hero-band{position:absolute;left:110px;top:283px;width:560px;height:66px;background:linear-gradient(90deg,rgba(160,15,35,0) 0%,rgba(160,15,35,.85) 20%,rgba(160,15,35,.85) 75%,rgba(160,15,35,0) 100%)}
.hero p{position:absolute;left:162px;top:434px;width:400px;color:#e6e6e6;font-size:14px;line-height:25px}
.mouse{position:absolute;left:587px;top:585px;width:26px;height:48px;border:2px solid #cfd2d6;border-radius:13px}
.mouse::after{content:"";position:absolute;left:10px;top:9px;width:2px;height:10px;background:#cfd2d6;border-radius:1px}

/* categories */
.cat-label{position:absolute;left:500px;width:200px;text-align:center}

/* about */
.about{position:absolute;left:0;top:929px;width:1200px;height:656px;background:linear-gradient(180deg,#d8d8d8,#ececec 50%,#d9d9d9)}
.section-title{font-size:36px;font-weight:300;color:var(--ink);letter-spacing:-.3px}
.section-title b{font-weight:700}
.about-text{position:absolute;left:700px;top:186px;width:340px;font-size:14px;line-height:25px;color:var(--text)}
.bullet{position:absolute;left:700px;font-size:14px;color:var(--text);display:flex;align-items:center;gap:10px}

/* products */
.card{position:absolute;top:1772px;width:235px;height:370px;text-align:center}
.card .img{position:absolute;left:0;top:0;width:235px;height:280px;background:var(--card-grey)}
.card .stars{position:absolute;left:0;width:100%;top:291px;color:#f5b400;font-size:11px;letter-spacing:1px}
.card .name{position:absolute;left:0;width:100%;top:307px;font-weight:700;font-size:18px}
.card .price{position:absolute;left:0;width:100%;top:342px;font-size:14px;font-weight:500;color:var(--red)}
.card .price s{color:var(--pink);margin-left:10px}
.card.featured{background:var(--red);top:1772px;height:368px;box-shadow:0 10px 25px rgba(0,0,0,.25)}
.card.featured .img{left:14px;top:14px;width:207px;height:266px;background:var(--pink)}
.card.featured .name,.card.featured .price{color:var(--white)}
.card.featured .price s{color:#f3a5b2}
.arrow-btn{position:absolute;width:38px;height:38px;border-radius:50%;background:var(--red);display:flex;align-items:center;justify-content:center}

/* sale */
.sale{position:absolute;left:0;top:2213px;width:1200px;height:463px;background:radial-gradient(ellipse at 20% 80%,#7a2a0a 0%,rgba(60,15,5,.9) 25%,transparent 55%),radial-gradient(ellipse at 90% 85%,#8a3a0c 0%,rgba(60,15,5,.8) 25%,transparent 55%),radial-gradient(ellipse at 95% 25%,#5c200a 0%,transparent 40%),#0a0807}
.sale-kicker{position:absolute;left:542px;top:2305px;color:var(--white);font-size:13px;font-weight:500;letter-spacing:2px}
.sale-title{position:absolute;left:542px;top:2322px;color:var(--white);font-size:37px;font-weight:300;line-height:50px;border-bottom:2px solid var(--white)}
.sale-title b{font-weight:700}
.sale-title .pct{color:var(--red);font-weight:700}
.sale p{position:absolute;left:542px;top:187px;width:440px;color:#e8e8e8;font-size:14px;line-height:25px}

.newsletter{position:absolute;left:162px;top:2613px;width:876px;height:147px;background:var(--white);border-radius:3px;box-shadow:0 8px 25px rgba(0,0,0,.15);z-index:2}
.newsletter h3{position:absolute;left:123px;top:32px;font-size:18px;font-weight:600}
.newsletter p{position:absolute;left:123px;top:64px;width:240px;font-size:13px;line-height:25px;color:var(--text)}
.nl-field{position:absolute;left:400px;top:52px;width:406px;height:46px;border-radius:23px;background:#f2f2f2;border:1px solid #e2e2e2}
.nl-field span{position:absolute;left:26px;top:13px;font-size:12px;color:#999}
.nl-field .nl-btn{position:absolute;right:-1px;top:-1px;width:120px;height:46px;border-radius:0 23px 23px 0;background:var(--red);color:var(--white);font-size:12px;font-weight:600;display:flex;align-items:center;justify-content:center}

/* blogs */
.blogs{position:absolute;left:0;top:2676px;width:1200px;height:710px;background:linear-gradient(180deg,#dedede,#ececec 50%,#d8d8d8)}
.blog{position:absolute;top:2935px;width:425px;height:327px;background:#ececec;box-shadow:0 6px 18px rgba(0,0,0,.12)}
.blog .img{position:absolute;left:0;top:30px;width:203px;height:268px}
.blog .date{position:absolute;left:0;top:30px;width:45px;height:46px;background:var(--red);color:var(--white);font-size:12px;font-weight:700;line-height:16px;padding:7px 0 0 14px}
.blog .meta{position:absolute;left:222px;top:30px;font-size:11px;color:var(--text);display:flex;gap:14px}
.blog .meta i{display:inline-block;width:9px;height:7px;background:var(--red);margin-right:5px;border-radius:1px}
.blog h4{position:absolute;left:222px;top:60px;width:180px;font-size:19px;font-weight:600;line-height:28px}
.blog p{position:absolute;left:222px;top:138px;width:170px;font-size:14px;line-height:25px;color:var(--text)}
.blog .arrow-btn{left:222px;top:248px;width:36px;height:36px}

/* features */
.feature{position:absolute;top:3448px;width:280px;text-align:center}
.feature h5{margin-top:20px;font-size:18px;font-weight:600}
.feature p{margin-top:12px;font-size:14px;line-height:25px;color:var(--text);padding:0 40px}

/* footer */
.footer{position:absolute;left:0;top:3745px;width:1200px;height:275px;background:var(--dark);color:var(--white)}
.footer h6{position:absolute;top:76px;font-size:14px;font-weight:600;letter-spacing:.3px}
.footer ul{position:absolute;top:112px;list-style:none;font-size:13px;line-height:25px;color:#e0e0e0}
.footer li::before{content:"";display:inline-block;width:5px;height:5px;border-radius:50%;background:var(--white);margin-right:9px;vertical-align:middle}
.social{position:absolute;top:3929px;width:32px;height:32px;border-radius:50%;background:var(--white)}
.copyright{position:absolute;left:0;top:4020px;width:1200px;height:40px;background:var(--red);color:var(--white);font-size:13px;display:flex;align-items:center;justify-content:center}
.copyright b{margin:0 4px;font-weight:700}
</style>
</head>
<body>

<!-- HERO -->
<section class="hero">
  <div class="hero-band"></div>
  <h1>COLLECTION<br><b>AND STYLE FOR</b><br>EVERYONE</h1>
  <p>Lorem Ipsum is simply dummy text of the printing and typesetting industry. Lorem Ipsum.</p>
  <div class="btn" style="left:162px;top:510px;width:167px;height:43px">EXPLORE NOW</div>
  <div class="ph" role="img" aria-label="White branded t-shirt product photo" style="left:745px;top:205px;width:307px;height:355px;background:linear-gradient(160deg,#f4f4f4,#d6d6d6);border-radius:14px 14px 6px 6px"></div>
  <div class="ph" role="img" aria-label="White branded cap product photo" style="left:630px;top:445px;width:160px;height:112px;background:linear-gradient(160deg,#f2f2f2,#cdcdcd);border-radius:70px 70px 12px 30px"></div>
  <div class="mouse"></div>
</section>

<header class="site-header">
  <div class="brand">BRISK PAILS</div>
  <nav class="nav">
    <a class="active" style="left:0">HOME</a>
    <a style="left:69px">PAGES</a>
    <a style="left:142px">SERVICES</a>
    <a style="left:233px">SHOP</a>
    <a style="left:300px">CONTACT US</a>
  </nav>
  <div class="search">
    <svg width="18" height="18" viewBox="0 0 18 18" fill="none" stroke="#ffffff" stroke-width="1.6"><circle cx="7.5" cy="7.5" r="5.5"/><path d="M11.5 11.5L16 16"/></svg>
  </div>
  <div class="btn" style="left:885px;top:20px;width:153px;height:44px">SHOP NOW</div>
</header>

<!-- CATEGORIES -->
<section class="categories">
  <svg class="abs" style="left:360px;top:705px" width="120" height="130" viewBox="0 0 120 130" fill="none">
    <circle cx="65" cy="55" r="32" fill="#f7d9de"/>
    <path d="M20 105 C25 70 45 55 68 58 C90 61 100 78 98 100 Z" stroke="#111" stroke-width="2.5"/>
    <path d="M20 105 C40 112 70 112 98 100" stroke="#111" stroke-width="2.5"/>
    <path d="M50 60 C45 75 44 92 48 108" stroke="#111" stroke-width="2"/>
  </svg>
  <svg class="abs" style="left:545px;top:700px" width="110" height="145" viewBox="0 0 110 145" fill="none">
    <circle cx="62" cy="30" r="26" fill="#f7d9de"/>
    <path d="M38 22 L55 36 L72 22 L95 32 L100 125 L10 125 L15 32 Z" stroke="#cc1430" stroke-width="2.5" stroke-linejoin="round"/>
    <path d="M55 36 V125 M28 45 V125 M82 45 V125" stroke="#cc1430" stroke-width="2"/>
    <circle cx="55" cy="55" r="2" fill="#cc1430"/><circle cx="55" cy="75" r="2" fill="#cc1430"/><circle cx="55" cy="95" r="2" fill="#cc1430"/>
  </svg>
  <svg class="abs" style="left:735px;top:712px" width="100" height="125" viewBox="0 0 100 125" fill="none">
    <circle cx="60" cy="25" r="22" fill="#f7d9de"/>
    <path d="M35 35 C35 15 65 15 65 35 L85 45 L88 115 L78 115 L76 75 L76 115 L24 115 L24 75 L22 115 L12 115 L15 45 Z" stroke="#111" stroke-width="2.5" stroke-linejoin="round"/>
    <path d="M35 35 C40 50 60 50 65 35 M45 48 V60 M55 48 V60" stroke="#111" stroke-width="2"/>
  </svg>
  <div class="cat-label" style="top:858px;font-weight:600;font-size:18px">T-Shirts</div>
  <div class="cat-label" style="top:884px;font-size:13px;color:var(--text)">150 Items</div>
</section>

<!-- ABOUT -->
<section class="about">
  <div class="abs" style="left:162px;top:156px;width:452px;height:425px;background:#b8b8b8;box-shadow:0 10px 25px rgba(0,0,0,.25)"></div>
  <div class="ph" role="img" aria-label="Man wearing a plain white t-shirt" style="left:205px;top:78px;width:365px;height:458px;background:linear-gradient(135deg,#6a6e73,#9ea2a6 45%,#5c6066)"></div>
  <div class="ph" role="img" aria-label="Red fire engine" style="left:5px;top:416px;width:365px;height:220px;background:linear-gradient(160deg,#d2262c,#8f0f14);border-radius:10px 40px 14px 14px"></div>
  <h2 class="section-title abs" style="left:700px;top:122px">ABOUT <b>US</b></h2>
  <p class="about-text">Lorem Ipsum is simply dummy text of the printing and typesetting industry. Lorem Ipsum has been the industry's standard dummy text ever since the 1500s, when an unknown printer took a galley of type and scrambled it to make a type specimen book. It has survived not only five centuries, but also the leap into electronic typesetting, remaining essentially unchanged</p>
  <div class="bullet" style="top:414px"><svg width="14" height="16" viewBox="0 0 14 16"><path d="M7 0 C9 5 13 6 13 11 A6 6 0 0 1 1 11 C1 8 3 6 4 4 C5 7 6 7 7 0Z" fill="#cc1430"/></svg>Lorem Ipsum is simply dummy text.</div>
  <div class="bullet" style="top:460px"><svg width="14" height="16" viewBox="0 0 14 16"><path d="M7 0 C9 5 13 6 13 11 A6 6 0 0 1 1 11 C1 8 3 6 4 4 C5 7 6 7 7 0Z" fill="#cc1430"/></svg>Lorem Ipsum is simply dummy text.</div>
  <div class="btn" style="left:705px;top:508px;width:165px;height:45px">EXPLORE NOW</div>
</section>

<!-- BEST SELLING -->
<section class="products">
  <svg class="abs" style="left:578px;top:1628px" width="44" height="60" viewBox="0 0 14 16"><path d="M7 0 C9 5 13 6 13 11 A6 6 0 0 1 1 11 C1 8 3 6 4 4 C5 7 6 7 7 0Z" fill="#f4d3d9"/></svg>
  <h2 class="section-title abs" style="left:0;width:1200px;text-align:center;top:1693px">BEST <b>SELLING PRODUCTS</b></h2>
  <div class="arrow-btn" style="left:163px;top:1892px"><svg width="16" height="12" viewBox="0 0 16 12" fill="none" stroke="#fff" stroke-width="1.8"><path d="M15 6H2M6 1L1 6L6 11"/></svg></div>
  <div class="arrow-btn" style="left:999px;top:1892px"><svg width="16" height="12" viewBox="0 0 16 12" fill="none" stroke="#fff" stroke-width="1.8"><path d="M1 6H14M10 1L15 6L10 11"/></svg></div>

  <div class="card" style="left:215px">
    <div class="img" role="img" aria-label="Light blue t-shirt"><div style="position:absolute;left:28px;top:40px;width:180px;height:200px;background:#b9dcf5;border-radius:20px 20px 6px 6px"></div></div>
    <div class="stars">★★★★★</div><div class="name">FIRE - CAP</div><div class="price">$150<s>$200</s></div>
  </div>
  <div class="card featured" style="left:482px">
    <div class="img" role="img" aria-label="White baseball cap"><div style="position:absolute;left:18px;top:70px;width:170px;height:120px;background:#f3f3f3;border-radius:80px 80px 12px 30px"></div></div>
    <div class="stars">★★★★★</div><div class="name">FIRE - CAP</div><div class="price">$150<s>$200</s></div>
  </div>
  <div class="card" style="left:750px">
    <div class="img" role="img" aria-label="Red hoodie"><div style="position:absolute;left:30px;top:28px;width:175px;height:225px;background:#d51f27;border-radius:60px 60px 8px 8px"></div></div>
    <div class="stars">★★★★★</div><div class="name">FIRE - CAP</div><div class="price">$150<s>$200</s></div>
  </div>
</section>

<!-- SALE -->
<section class="sale">
  <div class="ph" role="img" aria-label="Red branded cap" style="left:305px;top:12px;width:85px;height:85px;background:linear-gradient(160deg,#e5343a,#a51318);border-radius:45px 45px 8px 8px"></div>
  <div class="ph" role="img" aria-label="Red branded t-shirt" style="left:225px;top:117px;width:245px;height:270px;background:linear-gradient(160deg,#f03a30,#b8170f);border-radius:20px 20px 8px 8px"></div>
  <p>Lorem Ipsum is simply dummy text of the printing and typesetting industry. Lorem Ipsum has been the industry's</p>
  <div class="btn" style="left:542px;top:270px;width:158px;height:44px">SHOP NOW <svg width="7" height="11" viewBox="0 0 7 11" fill="none" stroke="#fff" stroke-width="1.8"><path d="M1 1L5.5 5.5L1 10"/></svg></div>
</section>
<div class="sale-kicker">NEW COLLECTION 2022</div>
<div class="sale-title">SALE <span style="font-weight:400">UPTO</span> <span class="pct">10%</span> <b>OFF</b></div>

<div class="newsletter">
  <svg class="abs" style="left:30px;top:36px" width="76" height="74" viewBox="0 0 76 74" fill="none" stroke="#cc1430" stroke-width="2.5" stroke-linejoin="round">
    <path d="M4 30 L38 6 L72 30 V70 H4 Z"/><path d="M4 30 L38 52 L72 30"/><path d="M4 70 L30 47 M72 70 L46 47"/>
    <rect x="16" y="14" width="44" height="18" fill="#fff"/><path d="M22 23 H54"/>
  </svg>
  <h3>Subscribe Newsletter</h3>
  <p>Sign up for new clothing ideas to your inbox every week</p>
  <div class="nl-field"><span>Email Address</span><div class="nl-btn">SUBSCRIBE</div></div>
</div>

<!-- BLOGS -->
<section class="blogs">
  <svg class="abs" style="left:578px;top:120px" width="44" height="60" viewBox="0 0 14 16"><path d="M7 0 C9 5 13 6 13 11 A6 6 0 0 1 1 11 C1 8 3 6 4 4 C5 7 6 7 7 0Z" fill="#f0c8cf"/></svg>
  <h2 class="section-title abs" style="left:0;width:1200px;text-align:center;top:182px">OUR <b>BLOGS</b></h2>
</section>
<article class="blog" style="left:162px">
  <div class="img" role="img" aria-label="Man in a grey t-shirt against a wall" style="background:linear-gradient(160deg,#9a9a96,#5d6770)"></div>
  <div class="date">20<br>Sep</div>
  <div class="meta"><span><i></i>Safety</span><span><i style="border-radius:50%"></i>20 Comments</span></div>
  <h4>Lorem Ipsum is Simple Text</h4>
  <p>Lorem Ipsum is simply dummy text of the printing and typesetting industry.</p>
  <div class="arrow-btn"><svg width="14" height="11" viewBox="0 0 16 12" fill="none" stroke="#fff" stroke-width="1.8"><path d="M1 6H14M10 1L15 6L10 11"/></svg></div>
</article>
<article class="blog" style="left:613px">
  <div class="img" role="img" aria-label="Man in a cap and t-shirt with red tint" style="background:linear-gradient(160deg,#b52a3a,#7a1420)"></div>
  <div class="date">15<br>Sep</div>
  <div class="meta"><span><i></i>Safety</span><span><i style="border-radius:50%"></i>20 Comments</span></div>
  <h4>Lorem Ipsum is Simple Text</h4>
  <p>Lorem Ipsum is simply dummy text of the printing and typesetting industry.</p>
  <div class="arrow-btn"><svg width="14" height="11" viewBox="0 0 16 12" fill="none" stroke="#fff" stroke-width="1.8"><path d="M1 6H14M10 1L15 6L10 11"/></svg></div>
</article>
<div class="btn" style="left:502px;top:3302px;width:197px;height:43px">VIEW MORE BLOGS <svg width="7" height="11" viewBox="0 0 7 11" fill="none" stroke="#fff" stroke-width="1.8"><path d="M1 1L5.5 5.5L1 10"/></svg></div>

<!-- FEATURES -->
<section class="features">
  <div class="feature" style="left:118px">
    <svg width="96" height="96" viewBox="0 0 96 96" fill="none">
      <path d="M82 30 A38 38 0 1 0 86 52" stroke="#cc1430" stroke-width="3"/><path d="M74 22 L84 30 L74 36" stroke="#cc1430" stroke-width="3"/>
      <circle cx="48" cy="48" r="30" stroke="#111" stroke-width="2.5" stroke-dasharray="5 5"/>
      <text x="48" y="56" text-anchor="middle" font-family="Poppins,sans-serif" font-weight="600" font-size="24" fill="#111">24/7</text>
    </svg>
    <h5>24/7 SUPPORT</h5>
    <p>Lorem Ipsum is simply dummy text of the printing and typesetting industry.</p>
  </div>
  <div class="feature" style="left:460px">
    <svg width="120" height="96" viewBox="0 0 120 96" fill="none" stroke-width="3" stroke-linejoin="round">
      <path d="M6 8 H72 V74 H6 Z M72 30 H98 L114 52 V74 H72" stroke="#111"/>
      <rect x="22" y="22" width="22" height="20" stroke="#cc1430"/><rect x="32" y="32" width="22" height="20" stroke="#cc1430"/>
      <circle cx="30" cy="80" r="9" fill="#fff" stroke="#111"/><circle cx="94" cy="80" r="9" fill="#fff" stroke="#111"/>
    </svg>
    <h5>WORLDWIDE SHIPPING</h5>
    <p>Lorem Ipsum is simply dummy text of the printing and typesetting industry.</p>
  </div>
  <div class="feature" style="left:802px">
    <svg width="100" height="96" viewBox="0 0 100 96" fill="none" stroke-width="3" stroke-linejoin="round">
      <rect x="6" y="36" width="66" height="46" rx="4" stroke="#111"/><path d="M6 50 H72 M16 68 H36" stroke="#111"/>
      <path d="M70 6 L92 14 V36 C92 50 80 58 70 62 C60 58 48 50 48 36 V14 Z" fill="#fff" stroke="#cc1430"/>
      <rect x="62" y="30" width="16" height="12" stroke="#cc1430"/><path d="M65 30 V25 A5 5 0 0 1 75 25 V30" stroke="#cc1430"/>
    </svg>
    <h5>SECURE PAYMENT</h5>
    <p>Lorem Ipsum is simply dummy text of the printing and typesetting industry.</p>
  </div>
</section>

<!-- FOOTER -->
<footer class="footer">
  <div class="abs" style="left:162px;top:60px;width:54px;height:54px;border-radius:50%;background:var(--white)"></div>
  <div class="abs" style="left:162px;top:128px;font-size:17px;font-weight:700;letter-spacing:.5px">BRISK PAILS APPAREL</div>
  <p class="abs" style="left:162px;top:170px;width:260px;font-size:13px;line-height:30px;color:#e0e0e0">Lorem ipsum dolor sit amet, consectetur adipiscing elit, sed do</p>
  <h6 style="left:450px">QUICK LINKS</h6>
  <ul style="left:452px"><li>Home</li><li>Pages</li><li>Services</li><li>Shop</li><li>Contact Us</li></ul>
  <h6 style="left:620px">OTHERS LINKS</h6>
  <ul style="left:622px"><li>Lorem</li><li>Ipsum</li><li>Simple</li><li>Dummy</li><li>Text</li></ul>
  <h6 style="left:816px">OUR NEWSLETTER</h6>
  <div class="abs" style="left:816px;top:108px;width:222px;height:45px;border-radius:23px;background:var(--white);overflow:hidden">
    <span class="abs" style="left:20px;top:14px;font-size:11px;font-style:italic;color:#888">Email Address</span>
    <div class="abs" style="right:0;top:0;width:52px;height:45px;background:var(--red);display:flex;align-items:center;justify-content:center">
      <svg width="16" height="16" viewBox="0 0 16 16"><path d="M15 1 L1 7 L6 9 L8 15 Z" fill="#fff"/></svg>
    </div>
  </div>
</footer>
<div class="social" style="left:817px" aria-label="Social link"></div>
<div class="social" style="left:879px" aria-label="Social link"></div>
<div class="social" style="left:942px" aria-label="Social link"></div>
<div class="social" style="left:1005px" aria-label="Social link"></div>
<div class="copyright">Copyright 2022 <b>BRISK PAILS APPAREL.</b> All Rights Reserved.</div>

</body>
</html>
```